Summer Music/Chorus/Choir Camp for Young Singers Ages 8-13

We need a flyer for a summer camp for young singers ages 8-13. We are nonprofit community children's chorus in Miami, FL. Our camp provides specialized training in music theory, sight-reading,and aural training through daily choral rehearsals in an environment that is both positive and a lot of fun! Our camp offers children the opportunity to come as they are, no matter the level of experience, and grow tremendously in their musicianship skills. In addition to this, our campers participate in song-writing, masterclasses, community performances, and media projects. The final design should be clean, fun, not too crowded, should appeal to boys and girls ages 8-13, and something someone that age would consider "cool" and not too childish. Drawings are cool, something different.
Updates

Target Market(s)

Ages 8-13 and parents of those kids.

Industry/Entity Type

Community

Requirements
Must have
• All info attached.
Nice to have
• Things that relate to music, especially related to singing/choirs
Should not have
• instruments, stock photos of children, or photos from our website (unless they are used very creatively), or photos in general. I've attached our previous camp flyer and our current organization flyer but I don't necessarily want this flyer to look like those.

```html
<!DOCTYPE html>
<html lang="en">
<head>
<meta charset="utf-8">
<title>Summer Camp — Bright Harmony Chorus</title>
<link href="https://fonts.googleapis.com/css2?family=Archivo+Black&family=Open+Sans:ital,wght@0,400;0,600;0,700;1,400;1,600&display=swap" rel="stylesheet">
<style>
  :root {
    --bg-light: #fbf5f8;
    --bg-lilac: #eddbe8;
    --purple: #7a4d92;
    --purple-deep: #5c3576;
    --violet-box: #9b78ad;
    --pink: #e894b3;
    --pink-dark: #c96b90;
    --white: #ffffff;
    --ink-soft: #8a6a9a;
  }
  * { margin: 0; padding: 0; box-sizing: border-box; }
  html, body { width: 849px; height: 1200px; overflow: hidden; }
  body {
    font-family: "Open Sans", Arial, sans-serif;
    color: var(--purple);
    background: var(--bg-light);
  }
  .flyer {
    position: relative;
    width: 849px;
    height: 1200px;
    overflow: hidden;
    background: radial-gradient(ellipse at 50% 40%, var(--bg-light) 0%, var(--bg-lilac) 75%, #e2c9dc 100%);
  }
  .note-field {
    position: absolute; inset: 0;
    background: radial-gradient(circle at 20% 30%, rgba(200,150,200,0.18), transparent 40%),
                radial-gradient(circle at 85% 55%, rgba(200,150,200,0.18), transparent 40%);
  }
  .dates {
    position: absolute; left: 34px; top: 30px;
    color: var(--purple);
    line-height: 1.1;
  }
  .dates .month { font-family: "Archivo Black", sans-serif; font-size: 36px; letter-spacing: 1px; }
  .dates .days { font-family: "Archivo Black", sans-serif; font-size: 26px; margin-top: 4px; }
  .dates .hours { font-weight: 700; font-size: 24px; margin-top: 8px; }
  .dates .ages { font-weight: 700; font-size: 24px; margin-top: 4px; }

  .brand {
    position: absolute; right: 60px; top: 60px;
    display: flex; align-items: center; gap: 12px;
  }
  .brand-dot { width: 34px; height: 34px; border-radius: 50%; background: var(--purple); flex: none; }
  .brand-name {
    font-family: "Open Sans", sans-serif; font-weight: 700;
    font-size: 34px; line-height: 1.05; color: var(--purple);
  }

  .singers-art {
    position: absolute; left: 170px; top: 170px;
    width: 520px; height: 540px;
    border-radius: 46% 46% 20% 20%;
    background: radial-gradient(ellipse at 50% 45%, #f3c9a6 0%, #e79a86 35%, #c55a6a 60%, rgba(200,110,150,0.2) 85%, transparent 100%);
  }

  .banner { position: absolute; left: 70px; top: 670px; width: 710px; height: 140px; }
  .banner-title {
    position: absolute; left: 0; right: 0; top: 722px;
    text-align: center;
    font-family: "Archivo Black", sans-serif;
    font-size: 56px; color: var(--white); letter-spacing: 1px;
  }

  .activities {
    position: absolute; left: 0; right: 0; top: 822px;
    text-align: center; font-weight: 600; font-size: 21px; color: var(--purple);
  }

  .about {
    position: absolute; left: 40px; right: 40px; top: 862px;
    background: var(--violet-box);
    color: var(--white);
    padding: 14px 28px;
    font-style: italic; font-size: 14.5px; line-height: 1.45;
    text-align: center;
  }

  .details { position: absolute; left: 40px; right: 40px; top: 1018px; display: flex; justify-content: space-between; }
  .cost { width: 360px; color: var(--purple); }
  .cost p { font-size: 19px; font-weight: 600; line-height: 1.4; }
  .cost .extra { font-size: 11px; font-weight: 400; margin-top: 10px; color: var(--ink-soft); }
  .venue {
    width: 360px; background: var(--violet-box); color: var(--white);
    padding: 12px 18px; font-size: 15.5px; line-height: 1.45; text-align: center;
  }

  .footer {
    position: absolute; left: 40px; right: 40px; top: 1160px;
    display: flex; align-items: center; justify-content: space-between;
  }
  .partners { display: flex; gap: 10px; }
  .partner-badge { width: 70px; height: 18px; background: #c4a9cf; }
  .partner-badge.small { width: 40px; }
  .legal { width: 360px; font-size: 9.5px; color: var(--ink-soft); text-align: center; }
</style>
</head>
<body>
<main class="flyer">
  <div class="note-field" role="img" aria-label="Scattered pastel music notes across a soft lilac background"></div>

  <section class="dates">
    <div class="month">JULY</div>
    <div class="days">18-19</div>
    <div class="hours">9AM-3PM</div>
    <div class="ages">(AGE[8-13] M-F)</div>
  </section>

  <div class="brand">
    <span class="brand-dot"></span>
    <span class="brand-name">Bright Harmony<br>Chorus</span>
  </div>

  <div class="singers-art" role="img" aria-label="Illustration of five cheerful children singing from red music folders"></div>

  <svg class="banner" viewBox="0 0 710 140" aria-hidden="true">
    <polygon points="0,60 90,60 90,130 0,130 30,95" fill="var(--pink-dark)"/>
    <polygon points="710,60 620,60 620,130 710,130 680,95" fill="var(--pink-dark)"/>
    <path d="M60,30 Q355,90 650,30 L650,110 Q355,160 60,110 Z" fill="var(--pink)"/>
  </svg>
  <div class="banner-title">SUMMER CAMP</div>

  <p class="activities">song-writing, masterclasses, community performances, and media projects</p>

  <p class="about">"Youth and children who love to sing will have a blast at our choral camp! Our music educators and industry professionals are dedicated to enhancing the lives of young singers through choral training which develops vocal technique, ear-training, music reading, and interpersonal skills. Activities are fun and interactive and former music training is not necessary. Singers in grades 2-8 are invited to attend! Register today!"</p>

  <section class="details">
    <div class="cost">
      <p>Cost- *$300 for 2-week session</p>
      <p>*Price does not include lunch.</p>
      <p class="extra">Extended hours available (7:30am-9:00am, 3pm-6pm) for an extra $30 per week.</p>
    </div>
    <address class="venue" style="font-style: normal;">
      Coral Bay Cultural Arts Center,<br>
      4820 SW 180th Street<br>
      Miami, FL 33100<br>
      Phone- 305.555.0142<br>
      Email- info@brightharmonychorus.org
    </address>
  </section>

  <footer class="footer">
    <div class="partners">
      <span class="partner-badge"></span>
      <span class="partner-badge small"></span>
    </div>
    <p class="legal">Bright Harmony Chorus is a 501(c)(3) nonprofit organization. Scholarships available to all who qualify.</p>
  </footer>
</main>
</body>
</html>
```